Hvac and insulation company needs good looking business card design

We are hvac and insulation company and looking for a new business cards that look to today standards designs

Target Market(s)

homeowners

Industry/Entity Type

Hvac

Contact Information for Business Card

Name: Dorian Velkova
Home comfort consultant
address: 4827 Marrow Ridge Rd #215 Oakland, CA 94611
office: 888-317-5069
cell: 510-642-1388
Lic.# 458127
Email: dorian@quarry-hvac.com
Web: quarry-hvac.com

Requirements
Must have
• clean and sleek look
Nice to have
• simple with a clean look
Should not have
• to busy business card

```html
<!DOCTYPE html>
<html lang="en">
<head>
<meta charset="utf-8">
<title>Quarry business card</title>
<link href="https://fonts.googleapis.com/css2?family=Roboto:wght@400;500;700&display=swap" rel="stylesheet">
<style>
  :root {
    --bg: #1f1f1f;
    --card-dark: #141414;
    --card-light: #fbfbfb;
    --orange: #f39220;
    --grey: #555555;
    --white: #ffffff;
  }
  * { margin: 0; padding: 0; box-sizing: border-box; }
  html, body {
    width: 1200px; height: 886px; overflow: hidden;
    background: var(--bg);
    font-family: "Roboto", Arial, sans-serif;
  }
  .canvas { position: relative; width: 1200px; height: 886px; }
  .card {
    position: absolute; width: 520px; height: 297px;
    border-radius: 16px; overflow: hidden;
  }
  .card-back {
    left: 90px; top: 90px; background: var(--card-dark);
    display: flex; flex-direction: column; align-items: center; justify-content: center;
  }
  .brand { display: flex; align-items: center; gap: 14px; }
  .brand-mark { width: 30px; height: 30px; background: var(--orange); }
  .brand-name { color: var(--orange); font-weight: 700; font-size: 52px; letter-spacing: -1px; line-height: 1; }
  .back-web {
    margin-top: 58px; color: var(--white); font-size: 12px; letter-spacing: 6px;
  }
  .card-front { left: 590px; top: 470px; background: var(--card-light); }
  .front-info { position: absolute; left: 30px; top: 34px; }
  .front-info .brand-name { font-size: 46px; }
  .holder-name {
    margin-top: 26px; color: var(--orange); font-size: 17px; font-weight: 500; text-transform: uppercase;
  }
  .holder-title { color: var(--grey); font-size: 13px; text-transform: uppercase; margin-top: 2px; }
  .address { margin-top: 16px; color: var(--grey); font-size: 12.5px; line-height: 1.35; width: 220px; }
  .contacts { margin-top: 12px; list-style: none; }
  .contacts li {
    display: flex; align-items: center; gap: 8px;
    color: var(--grey); font-size: 12.5px; line-height: 18px;
  }
  .contacts svg { width: 11px; height: 11px; fill: var(--orange); flex: none; }
  .accent-disc {
    position: absolute; right: -40px; top: 40px; width: 260px; height: 260px;
    border-radius: 50%; background: var(--orange);
  }
</style>
</head>
<body>
<div class="canvas">
  <section class="card card-back">
    <div class="brand">
      <span class="brand-mark"></span>
      <span class="brand-name">quarry</span>
    </div>
    <p class="back-web">quarry-hvac.com</p>
  </section>

  <section class="card card-front">
    <div class="front-info">
      <span class="brand-name">quarry</span>
      <p class="holder-name">Dorian Velkova</p>
      <p class="holder-title">Home Comfort Consultant</p>
      <p class="address">4827 Marrow Ridge Rd #215<br>Oakland, CA 94611</p>
      <ul class="contacts">
        <li><svg viewBox="0 0 12 12"><path d="M2 1l2 0 1 3-1.5 1a7 7 0 0 0 3.5 3.5L8 7l3 1v2a1 1 0 0 1-1 1A9 9 0 0 1 1 2a1 1 0 0 1 1-1z"/></svg>888-317-5069</li>
        <li><svg viewBox="0 0 12 12"><path d="M3 0h6a1 1 0 0 1 1 1v10a1 1 0 0 1-1 1H3a1 1 0 0 1-1-1V1a1 1 0 0 1 1-1zm0 2v7h6V2z"/></svg>510-642-1388</li>
        <li><svg viewBox="0 0 12 12"><path d="M3 0h6v3H3zM1 4h10v5H9v3H3V9H1zm3 4v3h4V8z"/></svg>510-642-1390</li>
        <li><svg viewBox="0 0 12 12"><path d="M0 2h12v8H0zm1 1l5 4 5-4z"/></svg>dorian@quarry-hvac.com</li>
        <li><svg viewBox="0 0 12 12"><circle cx="6" cy="6" r="6"/></svg>quarry-hvac.com</li>
      </ul>
    </div>
    <div class="accent-disc" role="img" aria-label="Large brand accent area"></div>
  </section>
</div>
</body>
</html>
```